KORVELTA Corporate Business Card

Modern business card design for company which focuses in the areas of Staffing, IT Consulting & Data Services. Please note: We are no longer using the IT subscript on the logo. All designs should have IT subscript removed.
Website: www.korveltait.example

```html
<!DOCTYPE html>
<html lang="en">
<head>
<meta charset="utf-8">
<title>KORVELTA Business Card</title>
<link rel="stylesheet" href="https://fonts.googleapis.com/css2?family=Montserrat:wght@400;500;600;700&display=swap">
<style>
  :root {
    --stage: #1c1d20;
    --card-white: #f4f5f6;
    --brand-blue: #2a9fd8;
    --brand-deep: #0a5a92;
    --back-top: #0e6fa6;
    --back-bottom: #063f72;
    --text-grey: #7a7d82;
  }
  * { margin: 0; padding: 0; box-sizing: border-box; }
  html, body {
    width: 1200px; height: 900px; overflow: hidden;
    background: var(--stage);
    font-family: "Montserrat", sans-serif;
  }
  .stage {
    width: 1200px; height: 900px;
    display: flex; flex-direction: column;
    align-items: center; justify-content: center; gap: 48px;
  }
  .card {
    width: 630px; height: 360px;
    border-radius: 30px;
    position: relative;
    overflow: hidden;
  }
  .card--front {
    background: linear-gradient(135deg, #e9eaec 0%, var(--card-white) 55%, #ffffff 100%);
    display: flex; flex-direction: column; align-items: center;
    padding-top: 66px;
  }
  .card--back {
    background: linear-gradient(160deg, var(--back-top) 0%, var(--back-bottom) 100%);
    display: flex; align-items: center; justify-content: center;
  }
  .brand {
    display: flex; align-items: center; gap: 14px;
  }
  .brand__square {
    width: 40px; height: 40px; border-radius: 6px;
    background: var(--brand-blue);
  }
  .brand__name {
    font-weight: 700; font-size: 56px; letter-spacing: 3px;
    color: var(--brand-blue); line-height: 1;
  }
  .card--back .brand__square { background: #2b8ccc; width: 52px; height: 52px; }
  .card--back .brand__name { color: #2b8ccc; font-size: 72px; }
  .person { margin-top: 38px; text-align: center; }
  .person__name {
    font-weight: 500; font-size: 21px; letter-spacing: 1.5px;
    color: var(--brand-blue); text-transform: uppercase;
  }
  .person__title {
    font-size: 15px; color: var(--text-grey); margin-top: 4px;
  }
  .divider {
    width: 30px; height: 3px; background: var(--brand-deep);
    margin: 14px auto 0;
  }
  .contact {
    margin-top: 26px; text-align: center;
    font-size: 14px; color: var(--text-grey); line-height: 1.7;
  }
  .contact .sep { color: var(--brand-blue); padding: 0 4px; }
  .contact .domain { color: var(--brand-deep); }
</style>
</head>
<body>
<main class="stage">
  <section class="card card--front" aria-label="Business card front">
    <div class="brand">
      <span class="brand__square"></span>
      <span class="brand__name">KORVELTA</span>
    </div>
    <div class="person">
      <p class="person__name">Marcus Dellaway</p>
      <p class="person__title">Chief Executive Officer</p>
      <div class="divider"></div>
    </div>
    <div class="contact">
      <p>418 Harlow St, Bramford, IN 47001, USA</p>
      <p>555-014-7720<span class="sep">/</span>contactus@korveltait.example<span class="sep">/</span>www.<span class="domain">korveltait</span>.example</p>
    </div>
  </section>
  <section class="card card--back" aria-label="Business card back">
    <div class="brand">
      <span class="brand__square"></span>
      <span class="brand__name">KORVELTA</span>
    </div>
  </section>
</main>
</body>
</html>
```